Create a Valdossi-looking dashboard for our Quiet Harbor Speedometer that can look similar to my AI-generated dashboard attached, but with: 1) clear borders on all four sides, 2) is created in a way that we can modify the numbers weekly, say maybe you create the graphic that we can inset the excel spreadsheet numbers into, but ideally mixed with the Valdossi look black leather bubble design shown in the dashboard?; 3) uses the exact numbers shown in the attachment; 4) the speedometer on top should have four equal colors of red on left (-1), then yellow (0), then light green (1), then medium green (2); 5) the gauge on the top left should be the graphic that includes 0-100% bar that is currently 33%, and right below that a -20 to +20 bar with the arrow pointing to 11.9%, with color coding similar to the graphic; 6) replace the Valdossi logo in the middle with a similar shaped shield with blue background with the "T" logo with the eagle inside it, like attached

```html
<!DOCTYPE html>
<html lang="en">
<head>
<meta charset="utf-8">
<title>Quiet Harbor Speedometer</title>
<link rel="stylesheet" href="https://fonts.googleapis.com/css2?family=Playfair+Display:wght@700;800&family=Inter:wght@400;500&family=Orbitron:wght@500;600&display=swap">
<style>
  :root {
    --leather: #b3242a;
    --leather-deep: #7c1418;
    --leather-light: #cf3a3f;
    --bezel: #c9c9cc;
    --bezel-dark: #5b5d61;
    --gauge-face: #15171a;
    --gold: #f2c230;
    --red: #e3261f;
    --yellow: #f3ee1a;
    --light-green: #8fe28a;
    --green: #3fbf4a;
    --mid-green: #36a83e;
    --navy: #1f3d9c;
    --grey-cell: #c9c9c9;
    --ink: #1b1b1b;
    --white: #f4f4f4;
    --stitch: #e8a1a3;
  }
  * { box-sizing: border-box; margin: 0; padding: 0; }
  html, body { width: 1200px; height: 960px; overflow: hidden; }
  body { background: var(--leather-deep); }

  .dashboard {
    position: relative;
    width: 1200px;
    height: 960px;
    border: 10px solid var(--bezel-dark);
    outline: 4px solid var(--bezel);
    outline-offset: -14px;
    overflow: hidden;
  }
  .leather-surface {
    position: absolute; inset: 0;
    background: radial-gradient(ellipse at 50% 40%, var(--leather-light), var(--leather) 45%, var(--leather-deep) 100%);
  }
  .gauge-cluster { position: absolute; left: 0; top: 0; width: 1180px; height: 540px; }

  .readout { font-family: "Orbitron", sans-serif; fill: var(--white); }
  .scale-label { font-family: "Orbitron", sans-serif; fill: var(--white); font-size: 13px; }
  .scale-label-small { font-family: "Orbitron", sans-serif; fill: var(--white); font-size: 11px; }
  .sector-label { font-family: "Orbitron", sans-serif; font-size: 26px; font-weight: 600; }
  .sector-label-light { fill: var(--white); }
  .sector-label-dark { fill: var(--ink); }
  .brand-name { font-family: "Inter", sans-serif; font-size: 15px; font-weight: 500; fill: var(--ink); letter-spacing: 1px; }

  .title {
    position: absolute; left: 0; right: 0; top: 548px;
    text-align: center;
    font-family: "Playfair Display", serif; font-weight: 800;
    font-size: 40px; color: var(--gold); letter-spacing: 0.5px;
    text-transform: uppercase;
  }
  .trend-panel {
    position: absolute; left: 130px; top: 612px; width: 920px; height: 300px;
    background: #111214;
    border: 6px solid var(--bezel);
    border-radius: 40px;
    padding: 22px 34px;
    box-shadow: 0 0 0 3px var(--bezel-dark), inset 0 0 20px #000;
  }
  .trend-table {
    width: 100%; height: 100%;
    border-collapse: separate; border-spacing: 6px 5px;
    font-family: "Inter", sans-serif; font-size: 18px; color: var(--ink);
    text-align: center;
  }
  .trend-table th {
    background: var(--navy); color: var(--white);
    font-family: "Playfair Display", serif; font-weight: 700;
    font-size: 17px; text-transform: uppercase; height: 44px;
  }
  .trend-table td { height: 44px; }
  .gear-turbo { background: var(--green); }
  .gear-accel { background: var(--light-green); }
  .gear-brakes { background: var(--yellow); }
  .gear-reverse { background: var(--red); }
  .cell-active { background: var(--green); }
  .cell-idle { background: var(--grey-cell); }
</style>
</head>
<body>
<main class="dashboard">
  <div class="leather-surface" role="img" aria-label="Red quilted leather upholstery with contrast stitching"></div>

  <svg class="gauge-cluster" viewBox="0 0 1180 540" aria-label="Gauge cluster">
    <!-- cluster housing -->
    <path d="M90 170 Q300 120 400 150 Q600 60 800 150 Q900 120 1090 170 L1090 520 L90 520 Z" fill="#2a2a2d" stroke="var(--bezel)" stroke-width="5" opacity="0.9"/>
    <path d="M110 190 Q300 145 410 172 Q600 90 790 172 Q900 145 1070 190" fill="none" stroke="var(--stitch)" stroke-width="2" stroke-dasharray="6 5"/>

    <!-- left gauge: 0-100% -->
    <g class="gauge-progress">
      <circle cx="240" cy="400" r="128" fill="var(--bezel)"/>
      <circle cx="240" cy="400" r="118" fill="var(--gauge-face)"/>
      <path d="M150 400 A90 90 0 0 1 176.4 336.4" fill="none" stroke="var(--green)" stroke-width="16"/>
      <path d="M176.4 336.4 A90 90 0 0 1 240 310" fill="none" stroke="var(--light-green)" stroke-width="16"/>
      <path d="M240 310 A90 90 0 0 1 303.6 336.4" fill="none" stroke="var(--yellow)" stroke-width="16"/>
      <path d="M303.6 336.4 A90 90 0 0 1 330 400" fill="none" stroke="var(--red)" stroke-width="16"/>
      <text class="scale-label" x="150" y="424" text-anchor="middle">0</text>
      <text class="scale-label" x="328" y="424" text-anchor="middle">100</text>
      <line x1="240" y1="400" x2="200" y2="330.7" stroke="var(--gold)" stroke-width="5" stroke-linecap="round"/>
      <circle cx="240" cy="400" r="12" fill="#333" stroke="var(--bezel)" stroke-width="2"/>
      <text class="readout" x="240" y="458" text-anchor="middle" font-size="32" font-weight="600">33%</text>
      <text class="readout" x="240" y="482" text-anchor="middle" font-size="15">(165/500)</text>
    </g>

    <!-- centre speedometer -->
    <g class="gauge-gear">
      <path d="M380 360 A220 220 0 0 1 820 360 Z" fill="var(--bezel)"/>
      <path d="M600 360 L400 360 A200 200 0 0 1 458.6 218.6 Z" fill="var(--red)"/>
      <path d="M600 360 L458.6 218.6 A200 200 0 0 1 600 160 Z" fill="var(--yellow)"/>
      <path d="M600 360 L600 160 A200 200 0 0 1 741.4 218.6 Z" fill="var(--light-green)"/>
      <path d="M600 360 L741.4 218.6 A200 200 0 0 1 800 360 Z" fill="var(--mid-green)"/>
      <text class="sector-label sector-label-light" x="470.7" y="315" text-anchor="middle">-01</text>
      <text class="sector-label sector-label-dark" x="546.4" y="245" text-anchor="middle">0</text>
      <text class="sector-label sector-label-dark" x="660" y="245" text-anchor="middle">01</text>
      <text class="sector-label sector-label-light" x="729.3" y="315" text-anchor="middle">02</text>
      <circle cx="539" cy="185" r="7" fill="var(--navy)"/>
      <text class="brand-name" x="552" y="190">QUIET HARBOR</text>
      <line x1="600" y1="360" x2="646.5" y2="260.3" stroke="var(--gold)" stroke-width="6" stroke-linecap="round"/>
      <path d="M552 360 A48 48 0 0 1 648 360 Z" fill="#222" stroke="var(--bezel)" stroke-width="4"/>
      <circle cx="600" cy="345" r="12" fill="#111"/>
    </g>

    <!-- right gauge: -20% to +20% -->
    <g class="gauge-change">
      <circle cx="950" cy="400" r="128" fill="var(--bezel)"/>
      <circle cx="950" cy="400" r="118" fill="var(--gauge-face)"/>
      <path d="M872.1 355 A90 90 0 0 1 926.7 313.1" fill="none" stroke="var(--green)" stroke-width="16"/>
      <path d="M926.7 313.1 A90 90 0 0 1 995 322.1" fill="none" stroke="var(--light-green)" stroke-width="16"/>
      <path d="M995 322.1 A90 90 0 0 1 1036.9 376.7" fill="none" stroke="var(--yellow)" stroke-width="16"/>
      <path d="M1036.9 376.7 A90 90 0 0 1 1027.9 445" fill="none" stroke="var(--red)" stroke-width="16"/>
      <text class="scale-label-small" x="898" y="374" text-anchor="middle">20%</text>
      <text class="scale-label-small" x="933" y="338" text-anchor="middle">10%</text>
      <text class="scale-label-small" x="982" y="350" text-anchor="middle">0%</text>
      <text class="scale-label-small" x="1006" y="388" text-anchor="middle">-10%</text>
      <text class="scale-label-small" x="1000" y="434" text-anchor="middle">-20%</text>
      <line x1="950" y1="400" x2="930" y2="354.2" stroke="var(--gold)" stroke-width="5" stroke-linecap="round"/>
      <circle cx="950" cy="400" r="12" fill="#333" stroke="var(--bezel)" stroke-width="2"/>
      <text class="readout" x="940" y="470" text-anchor="middle" font-size="32" font-weight="600">11.9%</text>
    </g>
  </svg>

  <h1 class="title">Quiet Harbor Speedometer</h1>

  <section class="trend-panel">
    <table class="trend-table">
      <thead>
        <tr><th>Gear</th><th>Current Trend</th><th>Last Trend Change</th></tr>
      </thead>
      <tbody>
        <tr><td class="gear-turbo">2 TURBO BOOST</td><td class="cell-active">BULL</td><td class="cell-active">Friday, August 15, 2025</td></tr>
        <tr><td class="gear-accel">1 ACCELERATOR PEDAL</td><td class="cell-idle">BULLISH</td><td class="cell-idle"></td></tr>
        <tr><td class="gear-brakes">0 BRAKES</td><td class="cell-idle">BEARISH</td><td class="cell-idle"></td></tr>
        <tr><td class="gear-reverse">-1 REVERSE</td><td class="cell-idle">BEAR</td><td class="cell-idle"></td></tr>
      </tbody>
    </table>
  </section>
</main>
</body>
</html>
```